Math Word Problems Make Your Palms Sweat??

I need a landing page for lead magnet download and email capture. Prospects will get here from QL ad. Landing page should be clean, simple and aimed at parents of Algebra 1 students. I will attach logo. Please use logo brand colors and fonts. The final design should be clear, easy to understand with struggling students and parents that don't know how to help. Copy should include: (lead magnet download info:) Number Story Rescue Pack with examples AND solutions, Conquer word problems with a step by step guide written by former teacher and full time math tutor.

Target Market(s)

Parents of struggling high school math/Algebra 1 students

Colors
33b8a4
ffffff

Requirements
Must have
• address pain points of:
struggling students
word problems causing angst
parents not knowing how to help their child

be clean, simple and easy to see what my message is via copy, images and feel of page

brand colors (ffffff, 5f5e60, 00a99d)and fonts (questrial, glacial indifference and arimo) from attached logo

clear call to action (download the pdf/lead magnet)
Nice to have
• bulleted points, not too wordy but clear message

related images/teens/struggling with math

my headshot if it looks appropriate on page

(I will likely have revisions once I see the first draft)
Should not have
• crowded
hard to read
message hard to decipher
busy
unclear call to action

```html
<!DOCTYPE html>
<html lang="en">
<head>
<meta charset="UTF-8">
<title>Clearpath Tutoring – Number Story Rescue Pack</title>
<link href="https://fonts.googleapis.com/css2?family=Arimo:wght@400;700&family=Roboto:wght@400;700&display=swap" rel="stylesheet">
<style>
  :root {
    --teal: #33b8a4;
    --brand-teal: #00a99d;
    --brand-grey: #5f5e60;
    --white: #ffffff;
    --panel: rgba(22, 24, 24, 0.9);
    --header-veil: rgba(236, 238, 238, 0.88);
    --board-dark: #2c3836;
    --board-mid: #485955;
    --floor-light: #a5785a;
    --floor-dark: #6a4530;
  }
  * { margin: 0; padding: 0; box-sizing: border-box; }
  html, body { width: 1200px; height: 800px; overflow: hidden; }
  body { font-family: "Roboto", Arial, sans-serif; position: relative; background: var(--board-dark); }

  .scene-backdrop { position: absolute; inset: 0; }
  .scene-board {
    position: absolute; left: 0; top: 0; width: 1200px; height: 658px;
    background: radial-gradient(ellipse at 60% 40%, var(--board-mid), var(--board-dark) 75%);
  }
  .scene-floor {
    position: absolute; left: 0; top: 658px; width: 1200px; height: 142px;
    background: linear-gradient(180deg, var(--floor-dark), var(--floor-light) 55%, var(--floor-dark));
  }
  .scene-figure {
    position: absolute; left: 620px; top: 275px; width: 200px; height: 470px;
    border-radius: 90px 90px 20px 20px;
    background: linear-gradient(180deg, #d9dcdc 0%, #b9bdbd 45%, #5f6262 60%, #4a4c4c 100%);
    opacity: 0.55;
  }

  .site-header {
    position: absolute; left: 0; top: 0; width: 1200px; height: 99px;
    background: var(--header-veil);
  }
  .brand-name {
    position: absolute; left: 132px; top: 30px;
    font-family: "Arimo", Arial, sans-serif; font-weight: 700; font-size: 28px;
    color: var(--brand-grey); letter-spacing: -0.5px;
  }
  .menu-toggle { position: absolute; left: 1020px; top: 25px; width: 46px; height: 46px; }

  .offer-panel {
    position: absolute; left: 138px; top: 252px; width: 428px; height: 406px;
    background: var(--panel);
  }
  .benefit-list { list-style: none; position: absolute; left: 48px; top: 52px; width: 360px; }
  .benefit {
    position: relative; padding-left: 24px;
    font-size: 19px; line-height: 26px; color: var(--white); font-weight: 400;
  }
  .benefit::before {
    content: ""; position: absolute; left: 0; top: 9px;
    border-left: 7px solid var(--white); border-top: 5px solid transparent; border-bottom: 5px solid transparent;
  }
  .benefit-divider { width: 365px; height: 1px; background: rgba(255,255,255,0.5); margin: 26px 0 26px -21px; }

  .signup-form { position: absolute; left: 27px; top: 267px; width: 375px; }
  .email-field {
    display: flex; align-items: center; gap: 12px;
    height: 47px; background: var(--white); padding-left: 18px;
    font-size: 13px; color: #333; letter-spacing: 0.5px;
  }
  .download-button {
    display: flex; align-items: center; justify-content: center;
    margin-top: 14px; height: 47px; background: var(--teal);
    color: var(--white); font-weight: 700; font-size: 22px; letter-spacing: 0.5px;
  }

  .tutor-headshot {
    position: absolute; left: 474px; top: 162px; width: 176px; height: 176px; border-radius: 50%;
    background: radial-gradient(circle at 50% 40%, #d9b7a3, #8a6a58 55%, #d8d6d2 75%);
    border: 3px solid #e9e9e9;
  }

  .prospectus-button {
    position: absolute; left: 142px; top: 682px; width: 375px; height: 60px;
    display: flex; align-items: center; justify-content: center;
    background: var(--teal); color: var(--white); font-weight: 700; font-size: 21px; letter-spacing: 0.5px;
  }
  .footer-tagline {
    position: absolute; left: 141px; top: 758px;
    font-weight: 700; font-size: 16px; color: var(--white); letter-spacing: 0.3px;
    text-shadow: 1px 1px 2px rgba(0,0,0,0.7);
  }
  .copyright {
    position: absolute; left: 867px; top: 767px; width: 203px; height: 33px;
    background: var(--white); border-radius: 5px 5px 0 0;
    display: flex; align-items: center; justify-content: center;
    font-family: "Arimo", Arial, sans-serif; font-size: 10px; color: #333;
  }
</style>
</head>
<body>
  <div class="scene-backdrop" role="img" aria-label="Chalkboard covered in math formulas above a wooden floor, with a man standing facing the board, hands on hips">
    <div class="scene-board"></div>
    <div class="scene-floor"></div>
    <div class="scene-figure"></div>
  </div>

  <header class="site-header">
    <div class="brand-name">Clearpath Tutoring</div>
    <svg class="menu-toggle" viewBox="0 0 46 46" aria-label="Menu">
      <circle cx="23" cy="23" r="21.5" fill="none" stroke="#33b8a4" stroke-width="2.5"/>
      <rect x="15" y="16" width="16" height="2.5" fill="#33b8a4"/>
      <rect x="15" y="21.7" width="16" height="2.5" fill="#33b8a4"/>
      <rect x="15" y="27.4" width="16" height="2.5" fill="#33b8a4"/>
    </svg>
  </header>

  <section class="offer-panel">
    <ul class="benefit-list">
      <li class="benefit">Number Story Rescue Pack with examples AND solutions</li>
      <li class="benefit-divider" aria-hidden="true"></li>
      <li class="benefit">Conquer word problems with a step by step guide written by former teacher and full time math tutor.</li>
    </ul>
    <form class="signup-form">
      <div class="email-field">
        <svg width="14" height="10" viewBox="0 0 14 10" aria-hidden="true">
          <rect width="14" height="10" fill="#555"/>
          <path d="M0 0 L7 5.5 L14 0" fill="none" stroke="#fff" stroke-width="1.2"/>
        </svg>
        <span>E MAIL ID</span>
      </div>
      <div class="download-button">DOWNLOAD</div>
    </form>
  </section>

  <div class="tutor-headshot" role="img" aria-label="Headshot of the tutor"></div>

  <div class="prospectus-button">GET YOUR PROSPECTUS</div>
  <p class="footer-tagline">LOREM IPSUM IS SIMPLY DUMMY TEXT OF THE PRINTING</p>
  <div class="copyright">Copyright © 2020 All Rights Reserved</div>
</body>
</html>
```